Mara Joss Advisory Business Cards

Hi - using the information and logo provided I require a two sided business card designed with the following information. The business card is a 'mini card' 3.5" x 1.25".

Front of card should be the logo attached but inverted (so the background is the peach colour and the logo white).

Back should have these details. If we can't fit the Instragram and Facebook part can we just put the little logos.

Ruth Penderby

Art and Design Consultant
Dealer - Curator - Events - Styling - Creative Sourcing

P: 0462 913 058
E: ruth@marajossadvisory.example
W: www.marajossadvisory.example
I (instagram image please): marajossadvisory F (Facebook image please): MaraJossAdvisor

Target Market(s)

Galleries, artists, art buyers, interior design clients, event managers, creative types

Industry/Entity Type

Business

```html
<!DOCTYPE html>
<html lang="en">
<head>
<meta charset="utf-8">
<title>Mara Joss Advisory – Mini Business Card</title>
<link rel="stylesheet" href="https://fonts.googleapis.com/css2?family=Tinos:wght@400&display=swap">
<style>
  :root {
    --stage: #75675f;
    --card-dark: #121212;
    --card-light: #f3f7fa;
    --panel: #ffffff;
    --peach: #f2b79c;
    --ink: #111111;
    --grey: #5b5b5b;
    --icon-green: #4caf3e;
    --icon-blue: #3b74c4;
    --icon-sky: #5aa6e0;
    --icon-slate: #6d6d6d;
  }
  * { box-sizing: border-box; margin: 0; padding: 0; }
  html, body { width: 1200px; height: 960px; overflow: hidden; }
  body {
    position: relative;
    background: var(--stage);
    font-family: "Tinos", "Times New Roman", serif;
  }

  /* Front of card */
  .card-front {
    position: absolute;
    left: 71px; top: 88px;
    width: 775px; height: 264px;
    background: var(--card-dark);
  }
  .brand-panel {
    position: absolute;
    left: 36px; top: 0;
    width: 281px; height: 218px;
    background: var(--panel);
    border-radius: 0 0 16px 16px;
    display: flex; flex-direction: column;
    align-items: center; justify-content: center;
    gap: 22px;
  }
  .brand-dot {
    width: 96px; height: 96px;
    border-radius: 50%;
    background: var(--peach);
  }
  .brand-name {
    font-size: 18px;
    font-weight: 400;
    letter-spacing: 2px;
    text-transform: uppercase;
    white-space: nowrap;
    text-align: center;
    color: var(--grey);
  }
  .rule {
    position: absolute;
    height: 5px;
    background: var(--peach);
  }
  .card-front .rule { left: 338px; width: 437px; }
  .card-front .rule.top { top: 28px; }
  .card-front .rule.bottom { top: 148px; }
  .identity {
    position: absolute;
    left: 338px; top: 42px;
    color: var(--peach);
  }
  .person-name { font-size: 34px; line-height: 40px; font-weight: 400; }
  .person-title { font-size: 20px; line-height: 24px; }
  .services { font-size: 16.5px; line-height: 20px; margin-top: 14px; white-space: nowrap; }

  /* Back of card */
  .card-back {
    position: absolute;
    left: 376px; top: 480px;
    width: 772px; height: 276px;
    background: var(--card-light);
  }
  .card-back .rule { left: 31px; width: 703px; }
  .card-back .rule.top { top: 25px; }
  .card-back .rule.bottom { top: 244px; }
  .mark-box {
    position: absolute;
    left: 63px; top: 50px;
    width: 183px; height: 162px;
    background: var(--panel);
    display: flex; flex-direction: column;
    align-items: center; justify-content: center;
    gap: 16px;
  }
  .mark-box .brand-dot { width: 90px; height: 90px; }
  .mark-box .brand-name { font-size: 12px; letter-spacing: 1px; }
  .contact-list {
    position: absolute;
    left: 326px; top: 48px;
    list-style: none;
  }
  .contact-item {
    display: flex; align-items: center;
    height: 33.5px;
    font-size: 20px;
    white-space: nowrap;
    color: var(--ink);
  }
  .contact-icon {
    width: 29px; height: 29px;
    margin-right: 17px;
    flex: none;
  }
</style>
</head>
<body>

  <section class="card-front" aria-label="Card front">
    <div class="brand-panel">
      <div class="brand-dot"></div>
      <div class="brand-name">Mara Joss Advisory</div>
    </div>
    <div class="rule top"></div>
    <div class="identity">
      <h1 class="person-name">Ruth Penderby</h1>
      <p class="person-title">(Art and Design Consultant)</p>
      <p class="services">Dealer | Curator | Events | Styling | Creative Sourcing</p>
    </div>
    <div class="rule bottom"></div>
  </section>

  <section class="card-back" aria-label="Card back">
    <div class="rule top"></div>
    <div class="mark-box">
      <div class="brand-dot"></div>
      <div class="brand-name">Mara Joss Advisory</div>
    </div>
    <ul class="contact-list">
      <li class="contact-item">
        <svg class="contact-icon" viewBox="0 0 29 29" aria-hidden="true">
          <rect width="29" height="29" rx="6" fill="var(--icon-green)"/>
          <path d="M9 7c1.5-.8 2.4 1.8 3 3 .4 1-1.4 1.6-1 2.6.8 2 2.4 3.6 4.4 4.4 1 .4 1.6-1.4 2.6-1 1.2.6 3.8 1.5 3 3-1 2-3.6 2.4-6 1-2.8-1.6-5-3.8-6.6-6.6C7 10.6 7 8.2 9 7z" fill="#fff"/>
        </svg>
        <span>0462 913 058</span>
      </li>
      <li class="contact-item">
        <svg class="contact-icon" viewBox="0 0 29 29" aria-hidden="true">
          <rect width="29" height="29" rx="6" fill="var(--icon-blue)"/>
          <rect x="5" y="8" width="19" height="13" fill="#fff"/>
          <path d="M5 8l9.5 7L24 8" fill="none" stroke="var(--icon-blue)" stroke-width="1.5"/>
        </svg>
        <span>ruth@marajossadvisory.example</span>
      </li>
      <li class="contact-item">
        <svg class="contact-icon" viewBox="0 0 29 29" aria-hidden="true">
          <rect width="29" height="29" rx="6" fill="var(--icon-sky)"/>
          <path d="M8 20a4 4 0 0 1 0-8 5.5 5.5 0 0 1 10.5-1.5A4.5 4.5 0 0 1 21 20z" fill="#fff"/>
        </svg>
        <span>www.marajossadvisory.example</span>
      </li>
      <li class="contact-item">
        <svg class="contact-icon" viewBox="0 0 29 29" aria-hidden="true">
          <rect width="29" height="29" rx="4" fill="var(--icon-blue)"/>
        </svg>
        <span>marajossadvisory</span>
      </li>
      <li class="contact-item">
        <svg class="contact-icon" viewBox="0 0 29 29" aria-hidden="true">
          <rect width="29" height="29" rx="4" fill="var(--icon-slate)"/>
        </svg>
        <span>MaraJossAdvisor</span>
      </li>
    </ul>
    <div class="rule bottom"></div>
  </section>

</body>
</html>
```